Upscale business cards needed for family office

We would like professional business cards created for employees of our family office. Relatively simple and straightforward, but also with a unique element to set them apart. Probably stick with neutral and simple colors that mesh well with the colors in the logo. We need space for the traditional elements, including name, title, address, email/phone number.

Industry/Entity Type

Business

Contact Information for Business Card

Space for name, title, phone number, email, address

```html
<!DOCTYPE html>
<html lang="en">
<head>
<meta charset="utf-8">
<title>Halden – Business Card</title>
<link rel="stylesheet" href="https://fonts.googleapis.com/css2?family=Noto+Sans:wght@300;400&display=swap">
<style>
  :root {
    --mint: #d9fcf0;
    --ink: #1a0f12;
    --slate: #1e2b2b;
    --accent-blue: #3fc1e0;
    --brand: #4a6670;
  }
  * { margin: 0; padding: 0; box-sizing: border-box; }
  html, body { width: 1200px; height: 700px; overflow: hidden; }
  body {
    position: relative;
    background: var(--mint);
    font-family: "Noto Sans", "Segoe UI", sans-serif;
    color: var(--ink);
  }
  .card-frame {
    position: absolute;
    left: 38px; top: 35px;
    width: 901px; height: 629px;
    border: 3px solid var(--slate);
    border-right: none;
  }
  .accent-rule {
    position: absolute;
    left: 937px; top: 0;
    width: 4px; height: 700px;
    background: var(--accent-blue);
  }
  .name-panel {
    position: absolute;
    left: 950px; top: 0;
    width: 250px; height: 700px;
    background: var(--slate);
  }
  .name-block {
    position: absolute;
    left: 988px; top: 160px;
    writing-mode: vertical-rl;
    color: var(--mint);
    font-weight: 300;
  }
  .person-name { font-size: 68px; line-height: 76px; margin-top: 40px; }
  .person-title { font-size: 45px; line-height: 50px; }
  .brand {
    position: absolute;
    left: 72px; top: 130px;
    display: flex; align-items: center; gap: 16px;
  }
  .brand-square {
    width: 52px; height: 52px;
    background: var(--accent-blue);
  }
  .brand-name {
    font-size: 46px; font-weight: 400;
    color: var(--brand);
    line-height: 1;
  }
  .contact-list { list-style: none; }
  .contact-item {
    position: absolute;
    left: 72px;
    display: flex; align-items: center;
    font-size: 33px;
    height: 60px;
  }
  .contact-item svg { width: 62px; height: 56px; flex: none; }
  .contact-item span { margin-left: 25px; }
  .item-phone { top: 266px; }
  .item-mobile { top: 371px; }
  .item-email { top: 473px; }
  .item-address { top: 572px; }
</style>
</head>
<body>
  <div class="card-frame"></div>
  <div class="accent-rule"></div>
  <div class="name-panel"></div>

  <div class="name-block">
    <div class="person-name">Ryan Cole</div>
    <div class="person-title">managing director</div>
  </div>

  <div class="brand">
    <div class="brand-square"></div>
    <div class="brand-name">Halden</div>
  </div>

  <ul class="contact-list">
    <li class="contact-item item-phone">
      <svg viewBox="0 0 62 56" aria-hidden="true">
        <path d="M4 18 Q31 2 58 18 L55 26 L44 24 L42 17 Q31 13 20 17 L18 24 L7 26 Z" fill="var(--ink)"/>
        <path d="M16 26 L46 26 L54 50 L8 50 Z" fill="var(--ink)"/>
        <circle cx="31" cy="37" r="8" fill="var(--mint)"/>
        <circle cx="31" cy="37" r="4" fill="var(--ink)"/>
      </svg>
      <span>428.555.0142</span>
    </li>
    <li class="contact-item item-mobile">
      <svg viewBox="0 0 62 56" aria-hidden="true">
        <rect x="18" y="-4" width="26" height="60" rx="5" fill="var(--ink)"/>
        <rect x="21" y="2" width="20" height="44" fill="var(--mint)"/>
        <rect x="27" y="49" width="8" height="3" rx="1.5" fill="var(--mint)"/>
      </svg>
      <span>209.555.0187</span>
    </li>
    <li class="contact-item item-email">
      <svg viewBox="0 0 62 56" aria-hidden="true">
        <rect x="2" y="10" width="58" height="38" rx="2" fill="var(--ink)"/>
        <path d="M5 13 L31 33 L57 13" fill="none" stroke="var(--mint)" stroke-width="2"/>
        <path d="M5 45 L24 28 M57 45 L38 28" stroke="var(--mint)" stroke-width="2"/>
      </svg>
      <span>rcole@haldenoffice.com</span>
    </li>
    <li class="contact-item item-address">
      <svg viewBox="0 0 62 56" aria-hidden="true">
        <path d="M31 54 L18 30 A15 15 0 1 1 44 30 Z" fill="var(--ink)"/>
        <circle cx="31" cy="22" r="5" fill="var(--mint)"/>
      </svg>
      <span>1580, NE 14th St, Larkton, WA 98012</span>
    </li>
  </ul>
</body>
</html>
```